Book Cover for Memoir: Sexual Assault and Traumatic Stress

I need a cover design for a memoir that is a victim's story of a sexual assault. I will need a print-on-demand cover, an eBook cover, and a 3D thumbnail image. The thumbnail and eBook cover will be used immediately, and the POD cover will be used in a few months with the full manuscript is ready. Therefore, I need an artist who is willing to make small adjustments if needed once the page count is set.

I have a image I have purchased that should give you an idea of the desired direction, but you can feel free to use your own images. I have attached some examples of book covers I like. I attached a color palette for fonts.

Overall Look: Fonts should be feminine and thin, but large to stand out. Look should be simple and elegant, and display and overall depressing feeling. There should be enough detail though to make it look professionally put together. Not TOO minimalistic.

I have also attached the Print Harbor templates if you choose to use those. If not, ensure there is an open place for the barcode on the bottom right.

Requirements
Must have
• Title: Beneath Quiet Rain
Subtitle: One Woman's Account of Fear, Guilt & Silence
Author: Dana Ruth Whitford
Audience: Mostly women 18-30
Quote (for the back): "I always thought I'd know how I'd react if I ever was raped. I was wrong. I've been wrong a lot lately."
Summary (back cover): When twenty-seven-year-old Dana Whitford wakes up with a gut-wrenching feeling, she has little memory of the horrifying events that occurred the night before. Days earlier, Dana was a spirited single mom who had abandoned her hometown to raise her daughter in the city and pursue her dreams. In the short months since Dana’s move to Seattle, she became the adored lover of a charismatic lawyer, started a new business, and finally felt life was going her way. So what happened to cause her to break?

In a gripping and heartbreaking narrative, Dana tells the true story of how her life unraveled from the traumatic events that took place that night and why what seems obvious to everyone else is impossible for Dana to believe. Beneath Quiet Rain is a chilling exploration of memory through trauma, trust in humanity, and a captivating story of strength and survival that appeals to the heart of fathers and mothers, sons and daughters, and men and women alike.
Nice to have
• BACK COVER: I'd like to have a photo on the back. This should depict the happy life of the main character before the sexual assault, and should be with her daughter. Or should be a nature scene that starts at the corner and blends into the rest of the cover. I have attached a possible image or you can use something you like.

```html
<!DOCTYPE html>
<html lang="en">
<head>
<meta charset="utf-8">
<title>Beneath Quiet Rain – Cover Design</title>
<link rel="stylesheet" href="https://fonts.googleapis.com/css2?family=Gelasio:wght@400&display=swap">
<style>
  :root {
    --page-bg: #ffffff;
    --rust-light: #d9a441;
    --rust-mid: #c07a2a;
    --rust-dark: #8a5a2a;
    --stone: #b8a98a;
    --page-edge: #cfc6b4;
    --shadow-purple: #4a3d6e;
    --shadow-black: #121014;
    --skin-rose: #9c4a5e;
    --sky-blue: #7fa6b8;
    --meadow: #8a8a4a;
    --type-white: #ffffff;
    --barcode-white: #ffffff;
  }
  * { margin: 0; padding: 0; box-sizing: border-box; }
  html, body {
    width: 1200px; height: 1000px; overflow: hidden;
    background: var(--page-bg);
  }
  body { position: relative; font-family: "Gelasio", Georgia, serif; color: var(--type-white); font-weight: 400; }
  h1, h2, h3 { font-weight: 400; }

  .cover-art {
    position: absolute; inset: 0;
    background:
      radial-gradient(ellipse 30% 40% at 68% 62%, var(--skin-rose) 0%, rgba(156,74,94,0.55) 40%, transparent 75%),
      radial-gradient(ellipse 42% 70% at 68% 52%, var(--shadow-black) 0%, var(--shadow-black) 50%, transparent 78%),
      radial-gradient(ellipse 32% 16% at 70% 5%, var(--shadow-purple) 0%, transparent 100%),
      linear-gradient(100deg, var(--rust-light) 0%, var(--rust-mid) 30%, var(--stone) 60%, var(--rust-mid) 85%, var(--rust-dark) 100%);
  }
  .title span { display: block; }

  /* Full print wrap */
  .print-wrap {
    position: absolute; left: 55px; top: 100px; width: 533px; height: 372px;
    overflow: hidden;
  }
  .back-panel {
    position: absolute; left: 0; top: 0; width: 245px; height: 100%;
    background: linear-gradient(90deg, var(--rust-light), var(--rust-mid) 60%, var(--rust-dark));
  }
  .back-photo {
    position: absolute; left: 110px; top: 0; width: 135px; height: 230px;
    background:
      linear-gradient(180deg, transparent 70%, var(--rust-mid) 100%),
      linear-gradient(90deg, var(--rust-mid) 0%, transparent 35%),
      linear-gradient(180deg, var(--sky-blue) 0%, #c9b27a 50%, var(--meadow) 100%);
  }
  .back-copy {
    position: absolute; left: 24px; top: 84px; width: 212px;
    font-size: 5.6px; line-height: 8.3px;
  }
  .back-copy p + p { margin-top: 8px; }
  .barcode-space {
    position: absolute; left: 158px; top: 314px; width: 80px; height: 48px;
    background: var(--barcode-white);
  }
  .spine {
    position: absolute; left: 245px; top: 0; width: 45px; height: 100%;
    background: linear-gradient(90deg, var(--rust-dark), var(--rust-mid) 50%, var(--stone));
  }
  .spine-title, .spine-author {
    position: absolute; writing-mode: vertical-rl; white-space: nowrap;
  }
  .print-wrap .spine-title { left: 10px; top: 16px; font-size: 21px; line-height: 24px; }
  .print-wrap .spine-author { left: 6px; top: 296px; font-size: 11px; line-height: 14px; }
  .front-panel {
    position: absolute; left: 290px; top: 0; width: 243px; height: 100%; overflow: hidden;
  }
  .front-panel .title { position: absolute; left: 10px; top: 36px; font-size: 44px; line-height: 46px; }
  .front-panel .subtitle { position: absolute; left: 10px; top: 182px; width: 160px; font-size: 9px; line-height: 11px; }

  /* Thumbnail (spine + front, flat) */
  .thumbnail {
    position: absolute; left: 140px; top: 540px; width: 300px; height: 415px; overflow: hidden;
  }
  .thumbnail .spine { left: 0; width: 55px; }
  .thumbnail .spine-title { left: 14px; top: 70px; font-size: 24px; line-height: 26px; }
  .thumbnail .spine-author { left: 8px; top: 330px; font-size: 12px; line-height: 15px; }
  .thumb-front { position: absolute; left: 55px; top: 0; width: 245px; height: 100%; overflow: hidden; }
  .thumb-front .title { position: absolute; left: 12px; top: 50px; font-size: 44px; line-height: 46px; }
  .thumb-front .subtitle { position: absolute; left: 12px; top: 196px; width: 170px; font-size: 10px; line-height: 12px; }

  /* eBook front cover */
  .ebook-cover {
    position: absolute; left: 607px; top: 107px; width: 541px; height: 731px; overflow: hidden;
  }
  .ebook-cover .title {
    position: absolute; left: 45px; top: 58px;
    font-size: 96px; line-height: 98px; letter-spacing: -1px;
  }
  .ebook-cover .subtitle {
    position: absolute; left: 47px; top: 360px; width: 280px;
    font-size: 17px; line-height: 21px;
  }
</style>
</head>
<body>

<section class="print-wrap" aria-label="Print cover wrap">
  <div class="back-panel" role="img" aria-label="Weathered rust-coloured wall texture"></div>
  <div class="back-photo" role="img" aria-label="Nature scene with a lone tree in a meadow under a blue sky, blending into the cover"></div>
  <div class="back-copy">
    <p>When twenty-seven-year-old Dana Whitford wakes up with a gut-wrenching feeling, she has little memory of the horrifying events that occurred the night before. Days earlier, Dana was a spirited single mom who had abandoned her hometown to raise her daughter in the city and pursue her dreams. In the short months since Dana's move to Seattle, she became the adored lover of a charismatic lawyer, started a new business, and finally felt life was going her way. So what happened to cause her to break?</p>
    <p>In a gripping and heartbreaking narrative, Dana tells the true story of how her life unraveled from the traumatic events that took place that night and why what seems obvious to everyone else is impossible for Dana to believe. Beneath Quiet Rain is a chilling exploration of memory through trauma, trust in humanity, and a captivating story of strength and survival that appeals to the heart of fathers and mothers, sons and daughters, and men and women alike.</p>
  </div>
  <div class="barcode-space"></div>

  <div class="spine">
    <div class="spine-title">Beneath Quiet Rain</div>
    <div class="spine-author">Dana<br>Ruth Whitford</div>
  </div>

  <div class="front-panel">
    <div class="cover-art" role="img" aria-label="Rusted, peeling wall with a dark opening where a woman sits hugging her knees"></div>
    <h2 class="title"><span>Beneath</span><span>Quiet</span><span>Rain</span></h2>
    <p class="subtitle">One Woman's Account of Fear, Guilt &amp; Silence</p>
  </div>
</section>

<section class="thumbnail" aria-label="Book thumbnail, spine and front">
  <div class="spine">
    <div class="spine-title">Beneath Quiet Rain</div>
    <div class="spine-author">Dana<br>Ruth Whitford</div>
  </div>
  <div class="thumb-front">
    <div class="cover-art" role="img" aria-label="Rusted, peeling wall with a dark opening where a woman sits hugging her knees"></div>
    <h3 class="title"><span>Beneath</span><span>Quiet</span><span>Rain</span></h3>
    <p class="subtitle">One Woman's Account of Fear, Guilt &amp; Silence</p>
  </div>
</section>

<section class="ebook-cover" aria-label="eBook front cover">
  <div class="cover-art" role="img" aria-label="Rusted, peeling wall with a dark opening where a woman sits hugging her knees"></div>
  <h1 class="title"><span>Beneath</span><span>Quiet</span><span>Rain</span></h1>
  <p class="subtitle">One Woman's Account of Fear, Guilt &amp; Silence</p>
</section>

</body>
</html>
```